Student project platform needs an awareness flyer

Tornuvel is a matchmaking and crowdfunding site for student projects. On this platform, students can team up with each other to invent a new product, innovate, or start a business. They can also raise funds for their project.

** I am in need of an 8x11" flyer to print and distribute digitally which notifies students of all different skill sets that this site exists.

The flyer should communicate that a diverse user base is being built on this site, with people who have skills in programming, engineering, design, business, finance, and so on.

The flyer should also be clean and modern, with an emphasis on creativity and innovation. I've attached the business' logo to give you an idea of the artistic style we have already established.

Target Market(s)

University students

Industry/Entity Type

Crowdfunding

Font styles to use
Serif
Sans Serif

Requirements
Must have
• * Clean and modern design
• * Color scheme of my logo: #336699 and #669933 (blue and green)
• * Convey that this site is for people of different skill sets: programming, engineering, design, business, finance, and so on.
• * See the attached "Tornuvel Copy.txt" for text to include on the flyer

```html
<!DOCTYPE html>
<html lang="en">
<head>
<meta charset="utf-8">
<title>Tornuvel – Calling All Students</title>
<link rel="stylesheet" href="https://fonts.googleapis.com/css2?family=Roboto+Condensed:wght@700&family=Open+Sans:wght@400;600&display=swap">
<style>
  :root{
    --brand-blue:#336699;
    --bright-blue:#1f8ad6;
    --deep-blue:#2a5d94;
    --brand-green:#669933;
    --footer-blue:#3a6aa1;
    --ink:#333333;
    --rule:#b9c2cc;
    --paper:#ffffff;
    --backdrop:#e8ebee;
  }
  *{box-sizing:border-box;margin:0;padding:0}
  html,body{width:1020px;height:1200px;overflow:hidden}
  body{background:var(--backdrop);position:relative;font-family:"Open Sans",Arial,sans-serif}

  .flyer{
    position:absolute;left:104px;top:41px;
    width:580px;height:798px;background:var(--paper);
    transform:scale(1.4);transform-origin:0 0;
    box-shadow:0 2px 6px rgba(0,0,0,.15);overflow:hidden;
  }
  .hero{position:absolute;left:0;top:0;width:580px;height:440px}

  .brand{position:absolute;left:0;width:580px;top:36px;text-align:center}
  .brand-dot{display:block;width:64px;height:64px;border-radius:50%;background:var(--brand-blue);margin:0 auto 10px}
  .brand-name{font-family:"Roboto Condensed",Arial,sans-serif;font-weight:700;font-size:31px;letter-spacing:1px;color:var(--brand-blue)}

  .headline{position:absolute;left:0;width:580px;top:278px;text-align:center;
    font-family:"Roboto Condensed",Arial,sans-serif;font-weight:700;font-size:37px;line-height:42px;color:var(--brand-blue)}

  .audience{position:absolute;left:0;width:580px;top:402px;text-align:center;font-family:"Roboto Condensed",Arial,sans-serif;font-weight:700}
  .audience-lead{font-size:34px;color:var(--brand-green);line-height:40px}
  .audience-goals{font-size:24.5px;color:var(--brand-blue);line-height:32px;margin-top:2px}

  .about{position:absolute;left:26px;top:500px;width:250px}
  .section-title{font-family:"Roboto Condensed",Arial,sans-serif;font-weight:700;font-size:31px;line-height:36px}
  .about .section-title{color:var(--brand-blue)}
  .about p{font-size:11.3px;line-height:17px;color:var(--ink);text-align:justify;margin-top:4px}
  .join{margin-top:20px}
  .join .section-title{color:var(--brand-green)}
  .join p{text-align:left;margin-top:6px}

  .divider{position:absolute;left:300px;top:493px;width:1px;height:242px;background:var(--rule)}

  .skills{position:absolute;left:322px;top:500px;width:182px}
  .skills-tag{position:relative;height:30px}
  .skills-tag svg{position:absolute;left:0;top:0}
  .skills-tag span{position:absolute;left:0;right:0;top:0;line-height:30px;text-align:center;color:#fff;
    font-family:"Roboto Condensed",Arial,sans-serif;font-weight:700;font-size:19px}
  .skill-list{list-style:none;margin-top:12px}
  .skill{display:flex;align-items:center;height:41.5px}
  .skill svg{flex:none;margin-left:13px}
  .skill-name{margin-left:24px;font-family:"Open Sans",Arial,sans-serif;font-weight:600;font-size:15.5px;color:var(--brand-green)}

  .footer{position:absolute;left:0;top:743px;width:580px;height:55px;background:var(--footer-blue);
    display:flex;align-items:center;justify-content:space-between;padding:0 20px 0 22px;color:#fff}
  .footer-phone{font-family:"Roboto Condensed",Arial,sans-serif;font-weight:700;font-size:22px}
  .footer-web{display:flex;align-items:center;gap:10px;font-family:"Open Sans",Arial,sans-serif;font-weight:600;font-size:15.5px}
</style>
</head>
<body>
  <main class="flyer">
    <svg class="hero" viewBox="0 0 580 440" xmlns="http://www.w3.org/2000/svg">
      <defs>
        <linearGradient id="photo-left" x1="0" y1="0" x2="1" y2="1">
          <stop offset="0" stop-color="#dfe6ee"/><stop offset=".55" stop-color="#b6c1cd"/><stop offset="1" stop-color="#8f9fb0"/>
        </linearGradient>
        <linearGradient id="photo-right" x1="1" y1="0" x2="0" y2="1">
          <stop offset="0" stop-color="#9aa77a"/><stop offset=".5" stop-color="#7d5a55"/><stop offset="1" stop-color="#5b6a82"/>
        </linearGradient>
        <linearGradient id="silver" x1="0" y1="0" x2="0" y2="1">
          <stop offset="0" stop-color="#f7f7f7"/><stop offset=".6" stop-color="#dedede"/><stop offset="1" stop-color="#c4c4c4"/>
        </linearGradient>
        <linearGradient id="band" x1="0" y1="0" x2="1" y2="0">
          <stop offset="0" stop-color="var(--deep-blue)"/><stop offset="1" stop-color="var(--bright-blue)"/>
        </linearGradient>
      </defs>
      <polygon role="img" aria-label="Photo of two smiling students holding a notebook" fill="url(#photo-left)" points="0,15 292,230 0,440"/>
      <polygon role="img" aria-label="Photo of students studying together with a tablet" fill="url(#photo-right)" points="580,15 292,230 580,430"/>
      <polygon fill="url(#silver)" points="292,230 83,380 508,380"/>
      <polygon fill="url(#band)" points="0,12 300,232 284,232 0,34"/>
      <polygon fill="url(#band)" points="580,12 580,34 300,232 284,232"/>
      <polygon fill="url(#band)" points="292,228 300,232 0,448 0,420"/>
      <polygon fill="url(#band)" points="284,232 292,228 580,420 580,442"/>
    </svg>

    <header class="brand">
      <span class="brand-dot"></span>
      <div class="brand-name">TORNUVEL</div>
    </header>

    <h1 class="headline">CALLING<br>ALL STUDENTS</h1>

    <section class="audience">
      <div class="audience-lead">WHO WANT TO</div>
      <div class="audience-goals">BUILD, INNOVATE, INVENT OR START A BUSINESS</div>
    </section>

    <section class="about">
      <h2 class="section-title">What is Tornuvel?</h2>
      <p>Tornuvel is a matchmaking and crowdfunding platform for student projects. It allows students to form teams of diverse skills and raise money to build, innovate, invent, or start a business</p>
      <div class="join">
        <h2 class="section-title">Join Tornuvel</h2>
        <p>to support and lend your skills to student projects!</p>
      </div>
    </section>

    <div class="divider"></div>

    <section class="skills">
      <div class="skills-tag">
        <svg width="182" height="30" viewBox="0 0 182 30">
          <polygon points="12,0 24,0 12,30 0,30" fill="var(--brand-green)"/>
          <polygon points="28,0 168,0 156,30 16,30" fill="var(--brand-blue)"/>
          <polygon points="172,0 182,0 170,30 160,30" fill="var(--brand-green)"/>
        </svg>
        <span>SKILLS</span>
      </div>
      <ul class="skill-list">
        <li class="skill">
          <svg width="32" height="32" viewBox="0 0 32 32"><rect x="6" y="6" width="20" height="20" rx="3" transform="rotate(45 16 16)" fill="var(--brand-blue)"/><rect x="10" y="11" width="12" height="8" fill="none" stroke="#fff" stroke-width="1.4"/><path d="M14 22h4M16 19v3" stroke="#fff" stroke-width="1.4"/></svg>
          <span class="skill-name">Programming</span>
        </li>
        <li class="skill">
          <svg width="32" height="32" viewBox="0 0 32 32"><rect x="6" y="6" width="20" height="20" rx="3" transform="rotate(45 16 16)" fill="var(--brand-blue)"/><circle cx="16" cy="10.5" r="2.2" fill="#fff"/><path d="M13 14h6v5h-1.5v5h-3v-5H13z" fill="#fff"/></svg>
          <span class="skill-name">Engineering</span>
        </li>
        <li class="skill">
          <svg width="32" height="32" viewBox="0 0 32 32"><rect x="6" y="6" width="20" height="20" rx="3" transform="rotate(45 16 16)" fill="var(--brand-blue)"/><path d="M11 11l10 10M21 11L11 21" stroke="#fff" stroke-width="2" stroke-linecap="round"/></svg>
          <span class="skill-name">Design</span>
        </li>
        <li class="skill">
          <svg width="32" height="32" viewBox="0 0 32 32"><rect x="6" y="6" width="20" height="20" rx="3" transform="rotate(45 16 16)" fill="var(--brand-blue)"/><path d="M11 21h10" stroke="#fff" stroke-width="1.4"/><path d="M11.5 18.5l3-3 2.5 2 4-4.5" fill="none" stroke="#fff" stroke-width="1.6"/></svg>
          <span class="skill-name">Business</span>
        </li>
        <li class="skill">
          <svg width="32" height="32" viewBox="0 0 32 32"><rect x="6" y="6" width="20" height="20" rx="3" transform="rotate(45 16 16)" fill="var(--brand-blue)"/><path d="M14 10h4l-1 2.5c3 1.5 4.5 4 4.5 6.5 0 2.5-2 3.5-5.5 3.5s-5.5-1-5.5-3.5c0-2.5 1.5-5 4.5-6.5z" fill="#fff"/></svg>
          <span class="skill-name">Finance</span>
        </li>
      </ul>
    </section>

    <footer class="footer">
      <span class="footer-phone">Call now:1234 567 890</span>
      <span class="footer-web">
        <svg width="20" height="20" viewBox="0 0 20 20" fill="none" stroke="#fff" stroke-width="1.3"><circle cx="10" cy="10" r="8.5"/><ellipse cx="10" cy="10" rx="3.8" ry="8.5"/><path d="M1.5 10h17M3 5.5h14M3 14.5h14"/></svg>
        www.tornuvel.com
      </span>
    </footer>
  </main>
</body>
</html>
```